facelift of our car wrap design - for Varno Klido L2

We would like to give our vehicles a facelift. Attached is our current advertising material.
Must-have: The paintwork of our vehicles is and will remain yellow. I would prefer to use the newer company logo, without the coloured bars, as shown in the attachment.
You can find further inspiration at www.plimtaaab.ch.

it should be a classic new design

• some advertising keywords

```html
<!DOCTYPE html>
<html lang="de">
<head>
<meta charset="utf-8">
<title>Varno Klido L2 – Fahrzeugbeschriftung PLIMTAAAB</title>
<link rel="stylesheet" href="https://fonts.googleapis.com/css2?family=Montserrat:wght@500;600;800&display=swap">
<style>
  :root {
    --paint-yellow: #e9dc1c;
    --wrap-black: #1e1c1a;
    --accent-yellow: #d8c81a;
    --glass: #4a4f4c;
    --trim: #2a2a2a;
    --tyre: #1a1a1a;
    --rim: #b9bcbd;
    --tail-red: #b3222a;
    --stage: #efefec;
  }
  html, body {
    margin: 0;
    padding: 0;
    width: 1200px;
    height: 488px;
    overflow: hidden;
    background: var(--stage);
  }
  .vehicle-wrap {
    display: block;
    width: 1200px;
    height: 488px;
    font-family: "Montserrat", sans-serif;
  }
  .van-paint { fill: var(--paint-yellow); }
  .wrap-band { fill: var(--wrap-black); }
  .bumper, .side-trim { fill: var(--trim); }
  .side-window { fill: var(--glass); }
  .mirror { fill: var(--wrap-black); }
  .headlight { fill: #3a3d40; }
  .taillight { fill: var(--tail-red); }
  .tyre { fill: var(--tyre); }
  .rim { fill: var(--rim); }
  .hub { fill: #2c2c2c; }
  .panel-line { fill: none; stroke: #a99f12; stroke-width: 1.2; }
  .brand-name {
    fill: var(--wrap-black);
    font-weight: 800;
    font-size: 92px;
  }
  .tagline {
    fill: var(--accent-yellow);
    font-weight: 500;
    font-size: 31px;
  }
  .web-address {
    fill: var(--accent-yellow);
    font-weight: 500;
    font-size: 22px;
  }
  .phone {
    fill: var(--accent-yellow);
    font-weight: 800;
    font-size: 20px;
  }
  .service-icon { fill: var(--wrap-black); }
  .service-label {
    fill: var(--wrap-black);
    font-weight: 600;
    font-size: 6px;
    letter-spacing: 0.3px;
  }
</style>
</head>
<body>
<svg class="vehicle-wrap" viewBox="0 0 1200 488" xmlns="http://www.w3.org/2000/svg" aria-label="Seitenansicht Fahrzeugbeschriftung Varno Klido L2">
  <defs>
    <clipPath id="body-shape">
      <path d="M42 372 L48 275 L70 222 L140 188 L250 150 L320 80 L350 52 Q370 44 420 43 L1120 58 Q1140 60 1148 80 L1160 190 L1168 330 L1166 378 L1120 382 L1000 384 Q990 330 935 322 Q880 330 868 395 L300 400 Q290 318 205 312 Q130 318 118 385 Z"/>
    </clipPath>
  </defs>

  <!-- body -->
  <g class="van-body">
    <path class="van-paint" d="M42 372 L48 275 L70 222 L140 188 L250 150 L320 80 L350 52 Q370 44 420 43 L1120 58 Q1140 60 1148 80 L1160 190 L1168 330 L1166 378 L1120 382 L1000 384 Q990 330 935 322 Q880 330 868 395 L300 400 Q290 318 205 312 Q130 318 118 385 Z"/>
    <g clip-path="url(#body-shape)">
      <polygon class="wrap-band" points="290,322 1200,150 1200,262 290,440"/>
      <polygon class="bumper" points="30,300 80,285 110,270 140,290 130,400 30,400"/>
      <polygon class="bumper" points="1010,330 1200,325 1200,400 1010,400"/>
    </g>
    <path class="side-trim" d="M345 380 L790 372 L800 388 L350 396 Z"/>
    <line class="panel-line" x1="555" y1="50" x2="555" y2="392"/>
    <line class="panel-line" x1="292" y1="170" x2="300" y2="395"/>
    <path class="side-window" d="M345 62 L530 60 Q537 60 537 70 L537 176 L282 166 Q300 110 345 62 Z"/>
    <path class="mirror" d="M308 132 Q330 128 334 145 L336 180 L312 178 Q300 160 308 132 Z"/>
    <path class="headlight" d="M75 208 L140 192 Q155 195 150 208 L118 225 L72 228 Z"/>
    <path class="taillight" d="M1128 190 L1152 190 L1158 282 L1132 282 Z"/>
  </g>

  <!-- wheels -->
  <g class="wheel">
    <circle class="tyre" cx="205" cy="398" r="74"/>
    <circle class="rim" cx="205" cy="398" r="46"/>
    <circle class="hub" cx="205" cy="398" r="14"/>
  </g>
  <g class="wheel">
    <circle class="tyre" cx="935" cy="405" r="70"/>
    <circle class="rim" cx="935" cy="405" r="44"/>
    <circle class="hub" cx="935" cy="405" r="13"/>
  </g>

  <!-- service row -->
  <g class="service-row">
    <g transform="translate(564 123)"><circle class="service-icon" r="12"/><text class="service-label" x="4" y="24" text-anchor="middle" transform="rotate(-9)">SANITÄR</text></g>
    <g transform="translate(631 112)"><circle class="service-icon" r="12"/><text class="service-label" x="4" y="24" text-anchor="middle" transform="rotate(-9)">HEIZUNG | KÄLTE</text></g>
    <g transform="translate(698 100)"><circle class="service-icon" r="12"/><text class="service-label" x="4" y="24" text-anchor="middle" transform="rotate(-9)">LÜFTUNG | KLIMA</text></g>
    <g transform="translate(765 88)"><circle class="service-icon" r="12"/><text class="service-label" x="4" y="24" text-anchor="middle" transform="rotate(-9)">KUNDENDIENST</text></g>
    <g transform="translate(829 77)"><circle class="service-icon" r="12"/><text class="service-label" x="4" y="24" text-anchor="middle" transform="rotate(-9)">BAUSPENGLEREI</text></g>
    <g transform="translate(899 66)"><circle class="service-icon" r="12"/><text class="service-label" x="4" y="24" text-anchor="middle" transform="rotate(-9)">DACHSERVICE</text></g>
  </g>

  <!-- brand & contact -->
  <g class="brand-block" transform="translate(368 275) rotate(-9.3)">
    <text class="brand-name" x="0" y="0" textLength="660" lengthAdjust="spacingAndGlyphs">PLIMTAAAB</text>
    <text class="tagline" x="20" y="48" textLength="654" lengthAdjust="spacing">HAUSTECHNIK + BAUSPENGLEREI</text>
    <text class="phone" x="140" y="76">+41 41 555 07 80</text>
    <text class="web-address" x="332" y="76" textLength="272" lengthAdjust="spacing">WWW.PLIMTAAAB.CH</text>
  </g>
</svg>
</body>
</html>
```